Gift voucher for a photo shoot, folding card DIN long (21 x 9.8 cm)

Hello, I'm a professional photographer and need a new design for my gift voucher card for a photo shoot. The design should be applicable to all types of photo shoots (neutral). I prefer a sophisticated design. The folded card should be printed on both sides.
My data should be included: Logo, Address: Birkwalder Strße 29, 39112 Talheim, Email: fotograf@ottobrenning.eu, Website: www.ottobrenning.eu Tel.: 0173 / 4958230
Updates

Please design the folding card in DIN long format (105 x 210 mm, landscape format). The card should open horizontally. Please design the front with the words "Gift voucher for you" and my logo. Please make the logo small – the words "Gift voucher" should be in the foreground.
The colors - use elegant gray with gold or white font color.
The inside should contain the words: Photo shoot for ........ worth .....€, as well as my logo.
My contact details should be on the back.

Target Market(s)

Private customer

Colors

Designer to choose only greyscale colors for use in the design.

Requirements
Must have
• Noble appearance, a gift voucher that one likes to give away, words: Gift voucher for you, photo shoot for ..., worth .......€
Nice to have
• Noble appearance of the gift voucher, a gift voucher that you like to give away
Should not have
• no pictures

```html
<!DOCTYPE html>
<html lang="de">
<head>
<meta charset="utf-8">
<title>Geschenkgutschein – Otto Brenning Fotograf</title>
<link href="https://fonts.googleapis.com/css2?family=Cinzel:wght@400;600&family=Open+Sans:wght@400&display=swap" rel="stylesheet">
<style>
  :root {
    --stage: #e6e7e8;
    --paper: #ffffff;
    --edge: #b9b9b9;
    --ink: #1f1f1f;
    --muted: #a9a9a9;
    --label: #c2c2c2;
    --headline: #b5b5b5;
    --gold-dark: #c2812c;
    --gold-light: #f4e7cf;
    --gold: #e9bb5c;
    --icon: #d7a64c;
    --serif: "Cinzel", "Trajan Pro", serif;
    --sans: "Open Sans", Arial, sans-serif;
  }
  * { box-sizing: border-box; margin: 0; padding: 0; }
  html, body { width: 1200px; height: 736px; overflow: hidden; }
  body { background: var(--stage); position: relative; font-family: var(--sans); }

  .spread { position: absolute; background: var(--paper); border: 1px solid var(--edge); overflow: hidden; }
  .spread--outside { left: 116px; top: 108px; width: 972px; height: 243px; }
  .spread--inside { left: 113px; top: 385px; width: 972px; height: 244px; }

  .panel { position: absolute; top: 0; height: 100%; width: 50%; }
  .panel--left { left: 0; }
  .panel--right { left: 50%; border-left: 1px solid #d4d4d4; }

  .back-panel { background: linear-gradient(225deg, #c3c3c3 0%, #e4e4e4 22%, #ffffff 48%); }
  .front-panel { background: linear-gradient(90deg, #cfcfcf 0%, #f2f2f2 14%, #ffffff 34%); }
  .inside-left { background: linear-gradient(90deg, #cdcdcd 0%, #ececec 22%, #ffffff 48%); }
  .inside-right { background: linear-gradient(90deg, #d3d3d3 0%, #f4f4f4 10%, #ffffff 24%); }

  .ribbon-band {
    position: absolute; left: 0; width: 100%; height: 6px;
    background: linear-gradient(90deg, var(--gold-dark) 0%, var(--gold-light) 30%, var(--gold) 55%, var(--gold-dark) 78%, var(--gold) 100%);
  }
  .spread--outside .ribbon-band { top: 92px; }
  .spread--inside .ribbon-band { top: 140px; }
  .ribbon-vertical {
    position: absolute; top: 0; left: 242px; width: 6px; height: 100%;
    background: linear-gradient(180deg, var(--gold-light) 0%, var(--gold) 35%, var(--gold-dark) 70%, var(--gold) 100%);
  }
  .bow {
    position: absolute; left: 212px; top: 78px; width: 66px; height: 64px;
    background: radial-gradient(ellipse at 50% 35%, #e6c891 0%, #f1deb8 50%, rgba(244,231,207,0) 72%);
  }

  .brand { position: absolute; display: flex; align-items: center; gap: 6px; transform: translateX(-50%); white-space: nowrap; }
  .brand__dot { width: 14px; height: 14px; border: 1.5px solid var(--ink); border-radius: 50%; }
  .brand__name { font-family: var(--serif); font-weight: 400; font-size: 12px; color: var(--ink); letter-spacing: 0.5px; }
  .front-panel .brand { left: 372px; top: 44px; }
  .inside-left .brand { left: 258px; top: 188px; }

  .headline {
    position: absolute; right: 42px; top: 118px; text-align: right;
    font-family: var(--serif); font-weight: 600; font-size: 26px; line-height: 30px; letter-spacing: 1px;
    color: var(--headline);
  }
  .headline__line { display: block; }
  .headline__accent { color: var(--gold-dark); }
  .headline-rule { position: absolute; left: 282px; right: 32px; top: 210px; height: 1px; background: linear-gradient(90deg, #e6d2a8, var(--gold)); }
  .web { position: absolute; left: 282px; right: 32px; top: 224px; text-align: center; font-size: 7.5px; letter-spacing: 1.4px; color: var(--muted); }

  .contact { position: absolute; right: 22px; top: 193px; list-style: none; }
  .contact li { display: flex; justify-content: flex-end; align-items: center; gap: 6px; height: 14px; font-size: 8.5px; color: var(--muted); }
  .contact svg { width: 9px; height: 9px; }

  .field { position: absolute; top: 69px; display: flex; align-items: baseline; font-family: var(--serif); font-size: 9.5px; letter-spacing: 0.8px; color: var(--label); }
  .field__line { flex: 1; border-bottom: 1px dotted #9c9c9c; margin-left: 4px; height: 8px; }
  .field__unit { color: #777; margin-left: 1px; font-family: var(--sans); }
  .field--for { left: 30px; width: 425px; }
  .field--worth { left: 32px; width: 421px; }
</style>
</head>
<body>

<section class="spread spread--outside" aria-label="Außenseite">
  <div class="panel panel--left back-panel">
    <div class="ribbon-band"></div>
    <ul class="contact">
      <li>0173 / 4958230
        <svg viewBox="0 0 10 10"><rect x="3" y="0.5" width="4.5" height="9" rx="0.8" fill="none" stroke="var(--icon)" stroke-width="1"/></svg></li>
      <li>Birkwalder Strße 29, 39112 Talheim
        <svg viewBox="0 0 10 10"><path d="M5 9.5 C2.5 6.3 2 5 2 3.8 A3 3 0 0 1 8 3.8 C8 5 7.5 6.3 5 9.5Z" fill="none" stroke="var(--icon)" stroke-width="1"/></svg></li>
      <li>fotograf@ottobrenning.eu
        <svg viewBox="0 0 10 10"><rect x="0.8" y="2" width="8.4" height="6" fill="none" stroke="var(--icon)" stroke-width="1"/><path d="M1 2.3 L5 5.6 L9 2.3" fill="none" stroke="var(--icon)" stroke-width="1"/></svg></li>
    </ul>
  </div>
  <div class="panel panel--right front-panel">
    <div class="ribbon-band"></div>
    <div class="ribbon-vertical"></div>
    <div class="bow" role="img" aria-label="Goldene Geschenkschleife am Bandkreuz"></div>
    <div class="brand"><span class="brand__dot"></span><span class="brand__name">Otto Brenning</span></div>
    <h1 class="headline">
      <span class="headline__line">Geschenk</span>
      <span class="headline__line">Gutschein</span>
      <span class="headline__line"><span class="headline__accent">für</span> Dich</span>
    </h1>
    <div class="headline-rule"></div>
    <p class="web">www.ottobrenning.eu</p>
  </div>
</section>

<section class="spread spread--inside" aria-label="Innenseite">
  <div class="panel panel--left inside-left">
    <div class="ribbon-band"></div>
    <p class="field field--for">Fotoshooting für<span class="field__line"></span></p>
    <div class="brand"><span class="brand__dot"></span><span class="brand__name">Otto Brenning</span></div>
  </div>
  <div class="panel panel--right inside-right">
    <div class="ribbon-band"></div>
    <p class="field field--worth">im Wert von<span class="field__line"></span><span class="field__unit">€</span></p>
  </div>
</section>

</body>
</html>
```